依頼詳細
コーディング等の作業はございません。載せたい項目・文章関係・動線については添付ラフの内容です。
ビジュアルのみの募集になりますが、もっと良くなりそうなご提案があれば変更してください。

下記の点を求めています。
・コンサル会社のサイトのようなイメージに変えたい!(経験豊富な専任コンサルタントがつき、いろいろアドバイスしてくれるので安心!)(忙しいお客さんや予算と実施のみが決まっているだけで具体的な提案を欲しがっているようなお客さんや納期がなく困っているお客さん等いろんなお客さんからの相談窓口)がほしい。
・自分で探したい人は、色んな用途で探しやすいサイトにしたい。(2軸のコンセプトのサイトを目指しています。)
・イメージカラーは、白ベースに赤

ターゲットは、25~45歳位の企業の販促担当者になります。
男女比は、半々程度です。

下記のようなサイトがいいと思っています。
https://torivane.net/
http://www.kumolo.jp/
サイトURL
http://www.sk-shokai.com/
ページ数
1ページ
希望イメージ
• +5 0 +5
• シンプル
複雑
• 単色
カラフル
• 暗い
明るい
• 日常
高級
• 遊び心
厳粛
• 未来的
伝統的
• 女性的
男性的
希望する色
赤系
納品ファイル
• イラストレーター形式 (.ai)
• フォトショップ形式 (.psd)
補足説明
・メリハリのある見やすいページにしたいです・
・頼りになる販促コンサルタントにおまかせできる(販促コンサルタントのブランディングをしっかりしたい)
・相談したくないもしくは相談前に自分で商品を探してみたい

この3点をしっかり表現出来ているサイトへのリニューアルを目指しています。

よろしくお願いいたします。
依頼公開後の追記内容
プロモエリアのコピーですが、

販促×お悩み相談!=集客商会

で、お願いします。
※もっといいご提案があれば変えていただいても大丈夫です。
必須ではありません。
当社の取扱商品や現在Web上で使用している素材が制作に必要な場合、
下記からダウンロードいただけます。

http://qv7.link/TpAx
パスワード:7wqe

今回の応募作品で制作していただく以外の目的には使用しないように
お願いいたします。
ダウンロード期限:2017年11月9日(木)

より大きいサイズの画像が必要な場合、
同じものをご用意できない可能性もありますが、ご相談くださいませ。
上記サンプルファイルのダウンロード期限が過ぎましたので
再びアップロードいたします。

http://rr828rr.info/K4mb
ダウンロード期限:2017年11月20日(月)

応募の期限は残り僅かですがどうぞよろしくお願いいたします。
■ 選んだ理由

お仕事が丁寧で、デザインもスッキリしていて、且つ訴求ポイントのわかりやすさとのバランスがとても気に入りました。

修正依頼に対するレスもとても早く助かりました。
また、機会がございましたらお願いできたら嬉しいです。
この度は、ありがとうございました。

■ 提案者全員のお礼・コメント

この度は弊社の集客商会のデザインコンペに参加いただき、誠にありがとうございました。
前回、集まりが悪いと思ってしまい途中で取り下げてしまったことが間違いだったと再認識しました。
今回も応募作品のレベルが高く選考するのにかなり迷ってしまいました。
選べなかった作品も素晴い作品が多くありました。
今回ご応募いただいた方々に感謝です。

ありがとうございました。
また、募集の機会がございましたら宜しくお願い致します。

```html
<!DOCTYPE html>
<html lang="ja">
<head>
<meta charset="utf-8">
<title>集客商会</title>
<link href="https://fonts.googleapis.com/css2?family=Noto+Sans+JP:wght@400;500;700;900&family=Montserrat:wght@500;700;800&display=swap" rel="stylesheet">
<style>
:root{
  --red:#d7222b;
  --red-dark:#b4161f;
  --ink:#333;
  --mute:#777;
  --line:#ddd;
  --pale:#f4f4f4;
  --pink:#fbe9ea;
  --bar:#3b3b3b;
  --white:#fff;
}
*{box-sizing:border-box;margin:0;padding:0}
html,body{width:1200px;height:4516px;overflow:hidden}
body{font-family:"Noto Sans JP",sans-serif;color:var(--ink);background:var(--white);font-size:13px}
section,header,footer,nav{position:relative;width:1200px;overflow:hidden}
.btn-red{display:inline-block;background:var(--red);color:var(--white);font-weight:700;text-align:center;border-radius:3px}
.sec-title{text-align:center;font-size:24px;font-weight:700;letter-spacing:.05em}
.sec-title::after{content:"";display:block;width:40px;height:3px;background:var(--red);margin:12px auto 0}

/* header */
.site-header{height:90px;border-bottom:1px solid var(--line)}
.header-strip{height:18px;background:var(--pale);font-size:10px;color:var(--red);padding:3px 20px;display:flex;justify-content:space-between}
.header-strip span:last-child{color:var(--mute)}
.header-main{display:flex;align-items:center;height:72px;padding:0 20px}
.logo{display:flex;align-items:center;gap:8px;width:250px}
.logo-mark{width:40px;height:40px;border-radius:50%;background:var(--red)}
.logo-name{font-size:30px;font-weight:900;color:var(--red);letter-spacing:.04em}
.global-nav{display:flex;flex:1;justify-content:center}
.global-nav a{font-size:11px;line-height:1.4;text-align:center;padding:0 14px;border-left:1px solid var(--line);color:var(--ink);text-decoration:none}
.global-nav a:last-child{border-right:1px solid var(--line)}
.header-tel{text-align:right;width:250px}
.tel-number{display:flex;align-items:center;justify-content:flex-end;gap:6px;font-size:30px;font-weight:700;color:var(--ink)}
.tel-sub{font-size:10px;color:var(--mute)}

/* hero */
.hero{height:446px}
.hero-visual{position:absolute;inset:0;background:linear-gradient(120deg,#f3e6da 0%,#f8f2ec 35%,#e9eef3 60%,#f6e2e2 100%)}
.hero-person{position:absolute;left:60px;top:40px;width:200px;height:406px;background:linear-gradient(#e3d8ce,#b9b2ad);border-radius:100px 100px 0 0}
.hero-band{position:absolute;left:0;right:0;top:170px;height:100px;background:rgba(255,255,255,.92);display:flex;align-items:center;justify-content:center}
.hero-copy{font-size:46px;font-weight:900;letter-spacing:.04em}
.hero-copy em{font-style:normal;color:var(--red)}

/* consult cards */
.consult{height:290px;background:var(--pale);display:flex;gap:12px;padding:22px 20px}
.consult-card{flex:1;position:relative;background:linear-gradient(#fff,#ececec);border:1px solid var(--line);overflow:hidden}
.consult-card .person{position:absolute;bottom:0;width:150px;height:215px;background:linear-gradient(#d7d2cf,#9c9796);border-radius:75px 75px 0 0}
.consult-card.left .person{left:16px}
.consult-card.right .person{right:16px}
.consult-card.center .person{right:24px}
.consult-card .body{position:absolute;top:26px;width:200px}
.consult-card.left .body{right:18px}
.consult-card.right .body{left:18px}
.badge{display:inline-block;background:var(--red);color:#fff;font-size:16px;font-weight:900;padding:3px 12px}
.area{font-size:40px;font-weight:900;color:var(--red);margin:6px 0 2px;line-height:1.1}
.consult-card .lead{font-size:14px;font-weight:700;line-height:1.5}
.consult-card .btn-red{margin-top:12px;font-size:12px;padding:7px 0;width:190px}
.consult-card.center{background:var(--white)}
.center-copy{position:absolute;top:90px;left:22px;font-size:15px;font-weight:700;line-height:1.7;width:190px}
.center-copy b{color:var(--red)}

/* bar nav */
.bar-nav{height:44px;background:var(--bar);display:flex;align-items:center;padding:0 20px}
.bar-nav a{color:#fff;font-size:12px;padding:0 22px;border-right:1px solid #555;text-decoration:none}
.bar-search{margin-left:auto;display:flex;align-items:center;background:#fff;height:26px;width:260px;border-radius:2px;padding:0 8px;font-size:11px;color:#999;justify-content:space-between}

/* features */
.features{height:120px;background:var(--pale);display:flex;gap:14px;padding:20px}
.feature{flex:1;background:#fff;border:1px solid var(--line);display:flex;align-items:center;justify-content:center;font-size:12px;color:var(--mute)}

/* strengths */
.strengths{height:640px;padding-top:44px}
.strengths .sec-title .num{color:var(--red);font-size:40px;font-family:"Montserrat",sans-serif;margin:0 6px}
.strengths-body{display:flex;padding:30px 130px 0}
.strength-photo{width:280px;height:440px;background:linear-gradient(#ece7e3,#b8b1ac);border-radius:140px 140px 0 0}
.strength-main{flex:1;padding-left:50px}
.points{display:flex;gap:26px}
.point{width:120px;height:120px;border-radius:50%;background:#fff;box-shadow:0 2px 10px rgba(0,0,0,.12);display:flex;flex-direction:column;align-items:center;justify-content:center;text-align:center;font-size:11px;font-weight:700;line-height:1.4}
.point .n{font-family:"Montserrat",sans-serif;font-size:36px;color:var(--red);font-style:italic;line-height:1}
.strength-text{font-size:11px;line-height:1.8;color:var(--mute);margin:22px 0 16px;width:460px}
.strength-sub{font-size:13px;font-weight:700;text-align:center;width:420px}
.strength-goods{width:420px;height:80px;margin:10px 0 20px;background:linear-gradient(90deg,#f1d9d9,#e7eef4,#f4eadc)}
.strength-main .btn-red{width:180px;padding:10px 0;font-size:14px;margin-left:120px}

/* reasons */
.reasons{height:480px;background:var(--pale);padding-top:44px}
.reason-list{display:flex;gap:24px;padding:40px 100px 0}
.reason{flex:1;text-align:center}
.reason-icon{width:70px;height:70px;margin:0 auto 16px;background:var(--white);border:2px solid var(--red);border-radius:8px}
.reason h3{font-size:13px;line-height:1.5;color:var(--red);margin-bottom:10px}
.reason p{font-size:10px;line-height:1.8;color:var(--mute);text-align:left}

/* sns */
.sns{height:300px;padding-top:40px}
.sns-list{display:flex;gap:30px;padding:30px 100px 0}
.sns-item{flex:1;text-align:center}
.sns-name{display:flex;align-items:center;justify-content:center;gap:8px;font-weight:700;font-size:16px;height:40px}
.sns-name i{width:22px;height:22px;border-radius:50%;background:var(--ink)}
.sns-box{border:1px solid var(--line);margin-top:14px;height:70px;display:flex;align-items:center;justify-content:center;font-size:11px;line-height:1.6}

/* consulting/search */
.cs{height:340px;display:flex;padding:40px 130px 0;gap:80px}
.cs-col{flex:1}
.cs-head{font-family:"Montserrat",sans-serif;font-size:30px;font-weight:700;letter-spacing:.1em;text-align:center;margin-bottom:20px}
.cs-lead{font-size:11px;color:var(--mute)}
.cs-lead b{font-size:24px;color:var(--ink);font-weight:900}
.cs-row{display:flex;align-items:center;gap:10px;margin-top:10px}
.cs-row .where{font-size:20px;font-weight:900;width:120px}
.cs-row .btn-red{flex:1;font-size:11px;padding:6px 0}
.search-box{display:flex;margin-top:12px;height:60px;border:1px solid var(--ink)}
.search-box .field{flex:1;font-size:10px;padding:8px;color:var(--mute);line-height:1.6}
.search-box .go{width:60px;background:var(--red);display:flex;align-items:center;justify-content:center}

/* news */
.news{height:310px;padding-top:36px;background:var(--pale)}
.news-list{display:flex;gap:24px;padding:34px 100px 0}
.news-item{flex:1;font-size:10px;line-height:1.8;color:var(--mute)}
.news-item time{display:block;font-weight:700;color:var(--ink);font-size:11px;margin-bottom:4px}

/* recommend */
.recommend{height:480px;padding-top:40px}
.carousel{position:relative;display:flex;gap:16px;padding:36px 80px 0}
.product{flex:1}
.product .ph{height:160px;background:linear-gradient(#f3eee6,#dbe3e6)}
.product p{font-size:10px;line-height:1.6;margin-top:8px}
.product .price{text-align:right;font-weight:700;font-size:12px;color:var(--red);margin-top:4px}
.arrow{position:absolute;top:130px;width:34px;height:34px;border-radius:50%;background:#555;display:flex;align-items:center;justify-content:center}
.arrow.prev{left:26px}.arrow.next{right:26px}

/* group */
.group{height:560px;padding-top:36px;background:var(--pale)}
.shop-grid{display:grid;grid-template-columns:repeat(5,1fr);gap:14px;padding:34px 60px 0}
.shop{height:92px;background:#fff;border:1px solid var(--line);position:relative}
.shop .ph{position:absolute;inset:26px 8px 8px;background:linear-gradient(90deg,#f2dada,#e6edf3)}
.shop span{position:absolute;left:8px;top:6px;font-size:11px;font-weight:700;color:var(--red)}

/* thanks */
.thanks{height:384px}
.thanks-visual{position:absolute;inset:0;background:linear-gradient(160deg,#f6e7d9 0%,#f0f3f6 40%,#f7e2e3 75%,#e9ecf0 100%)}
.thanks-word{position:absolute;font-family:"Montserrat",sans-serif;font-weight:800;color:var(--ink);letter-spacing:.12em;font-size:24px;white-space:nowrap}
.thanks-main{position:absolute;left:0;right:0;top:200px;text-align:center;font-family:"Montserrat",sans-serif;font-weight:800;font-size:84px;color:var(--red);letter-spacing:.02em;line-height:1}

/* footer */
.site-footer{height:36px;background:var(--red);color:#fff;font-size:11px;display:flex;align-items:center;justify-content:center}
</style>
</head>
<body>

<header class="site-header">
  <div class="header-strip"><span>販促品・ノベルティの相談窓口 集客商会</span><span>TEL 03-0000-0000 / FAX 03-0000-0001</span></div>
  <div class="header-main">
    <div class="logo"><span class="logo-mark"></span><span class="logo-name">集客商会</span></div>
    <nav class="global-nav" style="width:auto">
      <a href="#">初めての<br>方へ</a><a href="#">よくある<br>質問</a><a href="#">ご注文の<br>流れ</a><a href="#">ご相談<br>実績</a><a href="#">スタッフ<br>紹介</a><a href="#">会社<br>概要</a><a href="#">お問い<br>合わせ</a>
    </nav>
    <div class="header-tel">
      <div class="tel-number">
        <svg width="24" height="24" viewBox="0 0 24 24"><path fill="#d7222b" d="M6.6 10.8a15 15 0 0 0 6.6 6.6l2.2-2.2c.3-.3.7-.4 1-.2 1.1.4 2.3.6 3.6.6.6 0 1 .4 1 1V20c0 .6-.4 1-1 1C10.6 21 3 13.4 3 4c0-.6.4-1 1-1h3.5c.6 0 1 .4 1 1 0 1.3.2 2.5.6 3.6.1.3 0 .7-.2 1z"/></svg>
        0120-418-572
      </div>
      <div class="tel-sub">受付時間 平日 9:00〜18:00</div>
    </div>
  </div>
</header>

<section class="hero">
  <div class="hero-visual" role="img" aria-label="販促品・ノベルティ商品を並べた写真コラージュ"></div>
  <div class="hero-person" role="img" aria-label="資料を持つ女性コンサルタントの写真"></div>
  <div class="hero-band"><h1 class="hero-copy">販促 <em>×</em> お悩み相談！＝ <em>集客商会</em></h1></div>
</section>

<section class="consult">
  <div class="consult-card left">
    <div class="person" role="img" aria-label="全国担当の男性スタッフの写真"></div>
    <div class="body">
      <span class="badge">即商談！</span>
      <div class="area">全 国</div>
      <p class="lead">からのお問い合わせは<br>私にお任せください</p>
      <a class="btn-red">お問い合わせはこちら</a>
    </div>
  </div>
  <div class="consult-card center">
    <p class="center-copy">弊社は、<b>販促品のプロ</b>に<br>お任せください！</p>
    <div class="person" role="img" aria-label="笑顔の女性スタッフの写真"></div>
  </div>
  <div class="consult-card right">
    <div class="person" role="img" aria-label="東京23区担当の女性スタッフの写真"></div>
    <div class="body">
      <span class="badge">即商談！</span>
      <div class="area">東京23区</div>
      <p class="lead">からのお問い合わせは<br>私にお任せください</p>
      <a class="btn-red">お問い合わせはこちら</a>
    </div>
  </div>
</section>

<nav class="bar-nav">
  <a href="#">用途・シーンで探す</a><a href="#">価格帯で探す</a><a href="#">イベントで探す</a><a href="#">ターゲットで探す</a><a href="#">納期で探す</a>
  <div class="bar-search">何をお探しでしょうか？
    <svg width="14" height="14" viewBox="0 0 14 14"><circle cx="6" cy="6" r="4.5" fill="none" stroke="#666" stroke-width="1.6"/><path d="M9.5 9.5 13 13" stroke="#666" stroke-width="1.6"/></svg>
  </div>
</nav>

<section class="features">
  <div class="feature">特集</div><div class="feature">特集</div><div class="feature">特集</div><div class="feature">特集</div><div class="feature">特集</div><div class="feature">特集</div>
</section>

<section class="strengths">
  <h2 class="sec-title">集客商会の<span class="num">3</span>つの強み</h2>
  <div class="strengths-body">
    <div class="strength-photo" role="img" aria-label="ファイルを持つ女性コンサルタントの写真"></div>
    <div class="strength-main">
      <div class="points">
        <div class="point"><span class="n">1</span>数多くの<br>ご提案実績</div>
        <div class="point"><span class="n">2</span>幅広い<br>アイテム数</div>
        <div class="point"><span class="n">3</span>地域別専任<br>コンサルタント</div>
      </div>
      <p class="strength-text">企業の販促担当者様の様々なお悩みに対して、専任のコンサルタントが予算や納期に合わせた最適なご提案をいたします。具体的な内容が決まっていなくても安心してご相談ください。<br>オリジナル商品の企画から製作、納品まで一貫してサポートし、これまで多くの企業様のキャンペーンやイベントを成功に導いてまいりました。</p>
      <p class="strength-sub">こんな相談が多かったです！</p>
      <div class="strength-goods" role="img" aria-label="相談実績の販促品を並べた写真"></div>
      <a class="btn-red">ご相談実績</a>
    </div>
  </div>
</section>

<section class="reasons">
  <h2 class="sec-title">集客商会が選ばれる理由</h2>
  <div class="reason-list">
    <div class="reason"><div class="reason-icon"></div><h3>地域別専任スタッフが<br>ノベルティ製作を徹底サポート</h3><p>担当者が最初から最後まで責任を持って対応し、細かなご要望にも迅速にお応えします。</p></div>
    <div class="reason"><div class="reason-icon"></div><h3>製造業者から一括企画<br>製作でお得な価格</h3><p>工場との直接取引により中間コストを抑え、高品質な商品をお求めやすい価格でご提供します。</p></div>
    <div class="reason"><div class="reason-icon"></div><h3>いろいろな支払い方法<br>に対応</h3><p>銀行振込や後払いなど、企業様のご都合に合わせたお支払い方法をお選びいただけます。</p></div>
    <div class="reason"><div class="reason-icon"></div><h3>完全オリジナル商品の<br>独自のカスタマイズ</h3><p>形状や色、パッケージまで自由に設計でき、ブランドに合わせた一品を製作いたします。</p></div>
  </div>
</section>

<section class="sns">
  <h2 class="sec-title">SNS で実績やお客様の声などをご紹介</h2>
  <div class="sns-list">
    <div class="sns-item"><div class="sns-name"><i></i>PicLog</div><div class="sns-box">ご相談実績の<br>写真を公開中</div></div>
    <div class="sns-item"><div class="sns-name"><i></i>FaceBoard</div><div class="sns-box">新商品のお知らせと<br>お客様の声を紹介</div></div>
    <div class="sns-item"><div class="sns-name"><i></i>ChirpNet</div><div class="sns-box">今、こんな企画が人気！<br>最新情報を発信中</div></div>
    <div class="sns-item"><div class="sns-name"><i></i>ViewTube</div><div class="sns-box">オススメの商品を<br>動画でご紹介</div></div>
  </div>
</section>

<section class="cs">
  <div class="cs-col">
    <div class="cs-head">CONSULTING</div>
    <p class="cs-lead">具体的に決まっていなくて <b>悩んでいる…</b></p>
    <p class="cs-lead" style="margin-top:4px">まずは、お手軽お気軽にご相談下さい！</p>
    <div class="cs-row"><span class="where">全 国</span><a class="btn-red">お問い合わせはこちら</a></div>
    <div class="cs-row"><span class="where">東京23区</span><a class="btn-red">お問い合わせはこちら</a></div>
  </div>
  <div class="cs-col">
    <div class="cs-head">SEARCH</div>
    <p class="cs-lead">まずは <b>自分で探してみたい！</b></p>
    <p class="cs-lead" style="margin-top:4px">用途・価格・納期から検索</p>
    <div class="search-box">
      <div class="field">商品名やキーワードを入力してください。例：ボールペン、エコバッグ、名入れタオル</div>
      <div class="go"><svg width="22" height="22" viewBox="0 0 14 14"><circle cx="6" cy="6" r="4.5" fill="none" stroke="#fff" stroke-width="1.6"/><path d="M9.5 9.5 13 13" stroke="#fff" stroke-width="1.6"/></svg></div>
    </div>
  </div>
</section>

<section class="news">
  <h2 class="sec-title">お知らせ</h2>
  <div class="news-list">
    <div class="news-item"><time>2017.XX.XX</time>年末年始の営業日についてのご案内を掲載しました。</div>
    <div class="news-item"><time>2017.XX.XX</time>冬のキャンペーン向け新商品を追加しました。</div>
    <div class="news-item"><time>2017.XX.XX</time>東京23区の即日商談エリアを拡大しました。</div>
    <div class="news-item"><time>2017.XX.XX</time>ご相談実績ページを更新しました。</div>
    <div class="news-item"><time>2017.XX.XX</time>展示会用ノベルティ特集を公開しました。</div>
  </div>
</section>

<section class="recommend">
  <h2 class="sec-title">おすすめ商品</h2>
  <div class="carousel">
    <div class="arrow prev"><svg width="12" height="12" viewBox="0 0 12 12"><path d="M8 1 3 6l5 5" fill="none" stroke="#fff" stroke-width="2"/></svg></div>
    <div class="product"><div class="ph" role="img" aria-label="おすすめ商品の写真"></div><p>名入れ卓上カレンダー<br>オリジナル印刷対応</p><div class="price">100 円</div></div>
    <div class="product"><div class="ph" role="img" aria-label="おすすめ商品の写真"></div><p>名入れ卓上カレンダー<br>オリジナル印刷対応</p><div class="price">100 円</div></div>
    <div class="product"><div class="ph" role="img" aria-label="おすすめ商品の写真"></div><p>名入れ卓上カレンダー<br>オリジナル印刷対応</p><div class="price">100 円</div></div>
    <div class="product"><div class="ph" role="img" aria-label="おすすめ商品の写真"></div><p>名入れ卓上カレンダー<br>オリジナル印刷対応</p><div class="price">100 円</div></div>
    <div class="product"><div class="ph" role="img" aria-label="おすすめ商品の写真"></div><p>名入れ卓上カレンダー<br>オリジナル印刷対応</p><div class="price">100 円</div></div>
    <div class="product"><div class="ph" role="img" aria-label="おすすめ商品の写真"></div><p>名入れ卓上カレンダー<br>オリジナル印刷対応</p><div class="price">100 円</div></div>
    <div class="arrow next"><svg width="12" height="12" viewBox="0 0 12 12"><path d="M4 1l5 5-5 5" fill="none" stroke="#fff" stroke-width="2"/></svg></div>
  </div>
</section>

<section class="group">
  <h2 class="sec-title">集客商会グループ専門店</h2>
  <div class="shop-grid">
    <div class="shop"><span>オリジナルグッズ</span><div class="ph" role="img" aria-label="専門店の商品写真バナー"></div></div>
    <div class="shop"><span>うちわ専門店</span><div class="ph" role="img" aria-label="専門店の商品写真バナー"></div></div>
    <div class="shop"><span>タオル専門店</span><div class="ph" role="img" aria-label="専門店の商品写真バナー"></div></div>
    <div class="shop"><span>お菓子専門店</span><div class="ph" role="img" aria-label="専門店の商品写真バナー"></div></div>
    <div class="shop"><span>のぼり専門店</span><div class="ph" role="img" aria-label="専門店の商品写真バナー"></div></div>
    <div class="shop"><span>エコバッグ専門店</span><div class="ph" role="img" aria-label="専門店の商品写真バナー"></div></div>
    <div class="shop"><span>ボックスティッシュ</span><div class="ph" role="img" aria-label="専門店の商品写真バナー"></div></div>
    <div class="shop"><span>メモ帳専門店</span><div class="ph" role="img" aria-label="専門店の商品写真バナー"></div></div>
    <div class="shop"><span>カレンダー専門店</span><div class="ph" role="img" aria-label="専門店の商品写真バナー"></div></div>
    <div class="shop"><span>カイロ専門店</span><div class="ph" role="img" aria-label="専門店の商品写真バナー"></div></div>
    <div class="shop"><span>クリアファイル</span><div class="ph" role="img" aria-label="専門店の商品写真バナー"></div></div>
    <div class="shop"><span>ボールペン専門店</span><div class="ph" role="img" aria-label="専門店の商品写真バナー"></div></div>
    <div class="shop"><span>ステッカー専門店</span><div class="ph" role="img" aria-label="専門店の商品写真バナー"></div></div>
    <div class="shop"><span>マグカップ専門店</span><div class="ph" role="img" aria-label="専門店の商品写真バナー"></div></div>
    <div class="shop"><span>記念品専門店</span><div class="ph" role="img" aria-label="専門店の商品写真バナー"></div></div>
    <div class="shop"><span>ポーチ専門店</span><div class="ph" role="img" aria-label="専門店の商品写真バナー"></div></div>
    <div class="shop"><span>扇子専門店</span><div class="ph" role="img" aria-label="専門店の商品写真バナー"></div></div>
    <div class="shop"><span>付箋専門店</span><div class="ph" role="img" aria-label="専門店の商品写真バナー"></div></div>
    <div class="shop"><span>Tシャツ専門店</span><div class="ph" role="img" aria-label="専門店の商品写真バナー"></div></div>
    <div class="shop"><span>名刺専門店</span><div class="ph" role="img" aria-label="専門店の商品写真バナー"></div></div>
  </div>
</section>

<section class="thanks">
  <div class="thanks-visual" role="img" aria-label="販促品・ノベルティを円弧状に並べた写真コラージュ"></div>
  <span class="thanks-word" style="left:230px;top:40px">HIGH</span>
  <span class="thanks-word" style="left:250px;top:90px">QUALITY</span>
  <span class="thanks-word" style="left:0;top:320px;transform:rotate(-24deg)">ORIGINAL</span>
  <span class="thanks-word" style="right:-70px;top:240px;transform:rotate(68deg)">VARIETY OF NOVELTY</span>
  <div class="thanks-main">THANK YOU!</div>
</section>

<footer class="site-footer">Copyright © 2004-2017 集客商会 All Rights Reserved.</footer>

</body>
</html>
```